Letter Head Design

I need a letter head design based on my company logo that I attached.
Include phone number: (403)582-4316
Address: 347 14th Avenue NE, Calgary, Alberta, Canada, T3K 4R8

Industry/Entity Type

It Company

```html
<!DOCTYPE html>
<html lang="en">
<head>
<meta charset="utf-8">
<title>Lumora Interiors Corp. — Letterhead</title>
<link rel="stylesheet" href="https://fonts.googleapis.com/css2?family=Open+Sans:wght@400;600&display=swap">
<style>
  :root {
    --paper: #f4f4f5;
    --brand-blue: #1b5fae;
    --brand-green: #5cae3f;
    --band-blue: #1f63b2;
    --band-green: #5aad3e;
    --ink: #3a3a3a;
  }
  * { margin: 0; padding: 0; box-sizing: border-box; }
  html, body { width: 924px; height: 1200px; overflow: hidden; background: var(--paper); }
  .letterhead {
    position: relative;
    width: 924px;
    height: 1200px;
    background: var(--paper);
    font-family: "Open Sans", Arial, sans-serif;
    color: var(--ink);
  }
  .brand {
    position: absolute;
    top: 150px;
    left: 0;
    width: 100%;
    display: flex;
    justify-content: center;
    align-items: center;
    gap: 14px;
  }
  .brand-square {
    width: 30px;
    height: 30px;
    background: var(--brand-green);
    border-radius: 3px;
  }
  .brand-name {
    font-size: 34px;
    font-weight: 600;
    color: var(--brand-blue);
    letter-spacing: -0.5px;
  }
  .contact {
    position: absolute;
    top: 1128px;
    left: 26px;
    right: 26px;
    display: flex;
    justify-content: space-between;
    align-items: center;
    font-size: 15px;
  }
  .phone { display: flex; align-items: center; gap: 6px; letter-spacing: 1px; }
  .phone svg { width: 14px; height: 14px; }
  .address { letter-spacing: 0.1px; }
  .footer-bands {
    position: absolute;
    left: 0;
    top: 1148px;
    width: 924px;
    height: 22px;
  }
</style>
</head>
<body>
  <main class="letterhead">
    <header class="brand">
      <span class="brand-square"></span>
      <span class="brand-name">Lumora Interiors Corp.</span>
    </header>

    <footer>
      <div class="contact">
        <span class="phone">
          <svg viewBox="0 0 14 14" aria-hidden="true">
            <circle cx="7" cy="7" r="6.3" fill="none" stroke="#1b5fae" stroke-width="1.2"/>
            <path d="M5 3.6c-.6.2-1 .8-.9 1.6.3 2 1.9 4 3.9 4.9.7.3 1.4 0 1.8-.5l-1.3-1.2-.8.5C6.8 8.4 6 7.4 5.7 6.5l.7-.6z" fill="#1b5fae"/>
          </svg>
          (403)582-4316
        </span>
        <span class="address">347 14th Avenue NE, Calgary, Alberta, Canada, T3K 4R8</span>
      </div>
      <svg class="footer-bands" viewBox="0 0 924 22" preserveAspectRatio="none" aria-hidden="true">
        <polygon points="0,3 470,3 452,22 0,22" fill="var(--band-green)"/>
        <polygon points="482,3 924,3 924,22 464,22" fill="var(--band-blue)"/>
      </svg>
    </footer>
  </main>
</body>
</html>
```